Home Services- Spring Clean Options

Brightwell Crew provides a variety of Home Services- focused on cleaning & improving the exterior of the home:

 Power Washing- driveways, sidewalks, patios, decks, fence
 Fence Staining- make fence look new with variety of staining colors
 Gutter cleaning- important to make sure have proper Water Drainage
 Gutter Guard Installation- prevent damage to roof and house by keeping debris out of gutters and water flowing.
 Window Washing- our exterior washing team and reach the highest windows
 Landscape& Patio Lights- highlight areas for beauty and safety
Updates

We are are almost finished. Just please make sure you pay attention to the wording and grammer in Red thx

Target Market(s)

Middle to Upper level Home Owners (especially women)

Industry/Entity Type

Cleaning Services

Font styles to use
Serif
Sans Serif

Requirements
Must have
• Not be Cluttered- Clean friendly, professional look. Focus on the Professional

Info@GoBrightwellCrew.com
972-648-0000
Nice to have
• Pictures of services- these are just examples
Should not have
• Bigger and bolder Services & Specials. Want to Show all the Services we offer but do Not use too much detail- don't want it to look "cluttered"

```html
<!DOCTYPE html>
<html lang="en">
<head>
<meta charset="utf-8">
<title>Brightwell Crew – Home Cleaning Services</title>
<link href="https://fonts.googleapis.com/css2?family=Montserrat:wght@500;600;700;800;900&display=swap" rel="stylesheet">
<style>
  :root {
    --green: #0ea82f;
    --green-deep: #0b7d1c;
    --green-text: #158a2a;
    --blue: #0d3f8f;
    --blue-dark: #0a2f6e;
    --grey: #e6e6e6;
    --ink: #1d1d1d;
    --white: #ffffff;
  }
  * { box-sizing: border-box; margin: 0; padding: 0; }
  html, body { width: 783px; height: 1200px; overflow: hidden; background: #f2f2f2; }
  body { font-family: "Montserrat", Arial, sans-serif; color: var(--ink); }

  .flyer { position: relative; width: 783px; height: 1200px; background: var(--white); overflow: hidden; }

  .brand { position: absolute; left: 0; top: 0; width: 390px; height: 198px; display: flex; flex-direction: column; align-items: center; justify-content: center; gap: 12px; }
  .brand-dot { width: 46px; height: 46px; border-radius: 50%; background: var(--green); }
  .brand-name { font-weight: 800; font-size: 31px; color: var(--green-text); letter-spacing: -0.5px; }

  .rule-top { position: absolute; left: 0; top: 198px; width: 390px; height: 5px; background: var(--blue); }

  .hero { position: absolute; left: 0; top: 205px; width: 390px; height: 437px; background: linear-gradient(180deg, var(--green) 0%, var(--green-deep) 100%); color: var(--white); padding: 40px 0 0 47px; }
  .hero-title { font-weight: 800; line-height: 0.98; }
  .hero-title .big { display: block; font-size: 80px; letter-spacing: 1px; }
  .hero-title .mid { display: block; font-size: 49px; letter-spacing: 0.5px; margin-top: 4px; }
  .hero-divider { margin: 26px 0 28px; width: 290px; height: 1px; background: rgba(255,255,255,0.35); position: relative; }
  .hero-divider::before { content: ""; position: absolute; left: 0; top: -1px; width: 54px; height: 3px; background: var(--white); }
  .hero-sub { font-weight: 700; font-size: 25px; line-height: 1.3; }

  .photo { position: absolute; left: 389px; top: 63px; width: 394px; height: 579px; background: var(--blue); }
  .photo-scene { position: absolute; left: 24px; top: 36px; right: 0; bottom: 0; border: 10px solid #a7a294; border-right: none; border-bottom: none; background: radial-gradient(circle at 70% 30%, #3d7a2a 0%, #1d3b1a 45%, #0d1a12 100%); }

  .rule-bottom { position: absolute; left: 0; top: 644px; width: 783px; height: 6px; background: var(--blue); }

  .services { position: absolute; left: 0; top: 703px; width: 783px; height: 382px; background: var(--grey); }
  .services-tab { position: absolute; left: 220px; top: 678px; width: 345px; height: 68px; }
  .services-tab span { position: absolute; inset: 0; display: flex; align-items: center; justify-content: center; color: var(--white); font-size: 26px; font-weight: 500; letter-spacing: 0.5px; padding-top: 14px; }
  .services-tab b { font-weight: 800; margin-right: 8px; }

  .service-list { position: absolute; left: 47px; top: 768px; width: 710px; display: grid; grid-template-columns: 362px 348px; row-gap: 26px; }
  .service { display: flex; gap: 10px; }
  .service-icon { flex: none; width: 40px; height: 40px; }
  .service-name { font-size: 17.5px; font-weight: 600; color: var(--green-text); letter-spacing: 0.3px; margin-top: 9px; }
  .service-text { font-size: 14.5px; font-weight: 600; line-height: 1.25; margin-top: 5px; }
  .service-tags { display: grid; grid-template-columns: 102px 100px 80px; font-size: 14.5px; font-weight: 600; margin-top: 5px; row-gap: 3px; }
  .service-tags li { list-style: none; }
  .service-tags li::before { content: "•"; color: var(--green-text); margin-right: 5px; }

  .contact { position: absolute; left: 0; top: 1085px; width: 783px; height: 115px; }
  .phone-text { position: absolute; left: 100px; top: 1135px; font-size: 35px; font-weight: 700; color: var(--white); letter-spacing: 1px; }
  .web { position: absolute; left: 480px; top: 1128px; color: var(--white); font-size: 18px; font-weight: 600; line-height: 1.5; }
  .web div { display: flex; align-items: center; gap: 14px; }
</style>
</head>
<body>
<main class="flyer">
  <header class="brand">
    <span class="brand-dot"></span>
    <span class="brand-name">Brightwell Crew</span>
  </header>
  <div class="rule-top"></div>

  <section class="hero">
    <h1 class="hero-title"><span class="big">HOME</span><span class="mid">CLEANING</span><span class="mid">SERVICES</span></h1>
    <div class="hero-divider"></div>
    <p class="hero-sub">Brightwell Crew<br>provides a variety of<br>Home Services</p>
  </section>

  <div class="photo">
    <div class="photo-scene" role="img" aria-label="Cleaner in gloves washing a window with a squeegee, a lit garden at night beyond the glass"></div>
  </div>
  <div class="rule-bottom"></div>

  <section class="services">
  </section>
  <svg class="services-tab" viewBox="0 0 345 68" aria-hidden="true">
    <path d="M0 24 Q0 8 18 8 L327 8 Q345 8 345 24 L300 24 Q290 24 286 36 L278 58 Q274 68 262 68 L83 68 Q71 68 67 58 L59 36 Q55 24 45 24 Z" fill="var(--blue)"/>
  </svg>
  <div class="services-tab"><span><b>OUR</b> SERVICES</span></div>

  <div class="service-list">
    <div class="service">
      <svg class="service-icon" viewBox="0 0 40 40"><circle cx="20" cy="20" r="18" fill="#fff" stroke="var(--green-text)" stroke-width="2"/><circle cx="20" cy="20" r="12" fill="none" stroke="var(--blue)" stroke-width="2"/><path d="M15 14h6v12h-6zM22 16h4M22 20h4" stroke="#222" stroke-width="2" fill="none"/></svg>
      <div><h2 class="service-name">POWER WASHING</h2>
        <ul class="service-tags"><li>Driveways</li><li>Sidewalks</li><li>Patios</li><li>Decks</li><li>Fence</li></ul></div>
    </div>
    <div class="service">
      <svg class="service-icon" viewBox="0 0 40 40"><circle cx="20" cy="20" r="18" fill="#fff" stroke="var(--green-text)" stroke-width="2"/><circle cx="20" cy="20" r="12" fill="none" stroke="var(--blue)" stroke-width="2"/><path d="M14 16l6-3 6 3v8l-6 3-6-3z" stroke="#222" stroke-width="2" fill="none"/></svg>
      <div><h2 class="service-name">GUTTER GUARD INSTALLATION</h2>
        <p class="service-text">Prevent damage to roof and house<br>by keeping debris out of gutters<br>and water flowing.</p></div>
    </div>
    <div class="service">
      <svg class="service-icon" viewBox="0 0 40 40"><circle cx="20" cy="20" r="18" fill="#fff" stroke="var(--green-text)" stroke-width="2"/><circle cx="20" cy="20" r="12" fill="none" stroke="var(--blue)" stroke-width="2"/><path d="M14 16h12v9H14zM17 16v9M20 16v9M23 16v9" stroke="#222" stroke-width="1.6" fill="none"/></svg>
      <div><h2 class="service-name">FENCE STAINING</h2>
        <p class="service-text">Make fence look new with variety of<br>staining colors</p></div>
    </div>
    <div class="service">
      <svg class="service-icon" viewBox="0 0 40 40"><circle cx="20" cy="20" r="18" fill="#fff" stroke="var(--green-text)" stroke-width="2"/><circle cx="20" cy="20" r="12" fill="none" stroke="var(--blue)" stroke-width="2"/><path d="M14 14h12v12H14zM20 14v12M14 20h12" stroke="#222" stroke-width="2" fill="none"/></svg>
      <div><h2 class="service-name">WINDOW WASHING</h2>
        <p class="service-text">our exterior washing team and reach<br>the highest windows</p></div>
    </div>
    <div class="service">
      <svg class="service-icon" viewBox="0 0 40 40"><circle cx="20" cy="20" r="18" fill="#fff" stroke="var(--green-text)" stroke-width="2"/><circle cx="20" cy="20" r="12" fill="none" stroke="var(--blue)" stroke-width="2"/><path d="M14 15h12M14 20h12M14 25h12M20 13v14" stroke="#222" stroke-width="2.4" fill="none"/></svg>
      <div><h2 class="service-name">GUTTER CLEANING</h2>
        <p class="service-text">Important to make sure have proper<br>Water Drainage</p></div>
    </div>
    <div class="service">
      <svg class="service-icon" viewBox="0 0 40 40"><circle cx="20" cy="20" r="18" fill="#fff" stroke="var(--green-text)" stroke-width="2"/><circle cx="20" cy="20" r="12" fill="none" stroke="var(--blue)" stroke-width="2"/><circle cx="17" cy="17" r="3" fill="#222"/><circle cx="24" cy="16" r="2.5" fill="#222"/><path d="M12 26q5-7 10 0zM20 26q4-6 8 0z" fill="#222"/></svg>
      <div><h2 class="service-name">LANDSCAPE &amp; PATIO LIGHTS</h2>
        <p class="service-text">Highlight areas for beauty and safety</p></div>
    </div>
  </div>

  <svg class="contact" viewBox="0 0 783 115" aria-hidden="true">
    <rect x="0" y="0" width="783" height="115" fill="#fff"/>
    <polygon points="410,28 783,28 783,115 350,115" fill="var(--blue)"/>
    <polygon points="50,28 412,28 362,107 0,107 0,92 10,92" fill="var(--green)"/>
    <rect x="0" y="107" width="362" height="8" fill="var(--blue)"/>
    <path d="M68 58c2-2 4-2 5 0l3 4c1 2 0 3-1 4l-1 1c1 3 4 6 7 7l1-1c1-1 2-2 4-1l4 3c2 1 2 3 0 5l-2 2c-3 2-10-1-15-6s-8-12-6-15z" fill="#fff"/>
  </svg>
  <div class="phone-text">972-648-0000</div>
  <div class="web">
    <div><svg width="18" height="14" viewBox="0 0 18 14"><rect x="1" y="1" width="16" height="12" fill="none" stroke="#fff" stroke-width="2"/><path d="M1 1l8 7 8-7" fill="none" stroke="#fff" stroke-width="2"/></svg>Info@GoBrightwellCrew.com</div>
    <div><svg width="18" height="18" viewBox="0 0 18 18"><circle cx="9" cy="9" r="7.5" fill="none" stroke="#fff" stroke-width="1.6"/><ellipse cx="9" cy="9" rx="3.5" ry="7.5" fill="none" stroke="#fff" stroke-width="1.4"/><path d="M1.5 9h15" stroke="#fff" stroke-width="1.4"/></svg>www.gobrightwellcrew.com</div>
  </div>
</main>
</body>
</html>
```